I need to launch a new website that more accurately reflects what we do as a business. We are an IT Reseller that specialises in delivering innovative solutions covering supply, implementation and support. My current website is www.vornetikx.com and was something I designed myself on the Hub Nimbo website. This was fine for the first 2 years but now I need something more professional and detailed. A couple of websites for companies similar to Brindle KTR are www.quarvolen.co.uk and www.ferrimund.co.uk. By looking at these it will hopefully give you an idea as to what I am trying to achieve.

Target Market(s)

UK based companies with between 30-250 employees, no fixed vertical

Coding

Coded - Design and coding required

Number of Pages Required

4 page

Font styles to use
Sans Serif

Colors
33a6d7
0592cd
85cae6

Requirements
Must have
• Contact details page to include a "Get in touch with us " section, About Us page, IT Support page to include the headings 1/ Proactive Monitoring 2/ 24 x 7 Support 3/ Security and Data Back-up 4/ Built-in Compliance (GDPR) 5/ Responsive IT Support. I am happy to provide the wording for these headings.
Clean crisp home screen with a Menu offering the requested drop down options.
Nice to have
• Easy to navigate site with a good flow. I have updated a page regarding cloud services, this would be great to have as a separate drop down menu option. I would like to have different Cloud logo's in ideally the Brindle Blue colour. Can you please add the photograph of Thornwick Lodge which is my office in the contact us page.
Should not have
• I definitely DO NOT want a photo/view of London on the home page!!

```html
<!DOCTYPE html>
<html lang="en">
<head>
<meta charset="utf-8">
<title>Brindle KTR – Experienced, Personalised IT Consulting</title>
<link rel="stylesheet" href="https://fonts.googleapis.com/css2?family=Montserrat:ital,wght@0,400;0,500;0,600;0,700;1,400&display=swap">
<style>
:root{
  --blue:#0592cd;
  --blue-mid:#33a6d7;
  --blue-light:#85cae6;
  --ink:#222;
  --muted:#8a8a8a;
  --band:#f7f7f7;
  --field:#f4f4f4;
  --white:#fff;
}
*{box-sizing:border-box;margin:0;padding:0}
html,body{width:1200px;height:3628px;overflow:hidden}
body{background:var(--white);font-family:'Montserrat',sans-serif;color:var(--ink);position:relative}
.abs{position:absolute}
.brand{display:flex;align-items:center;gap:14px;font-weight:600;color:var(--ink)}
.brand-dot{border-radius:50%;background:var(--blue)}
.board-brand{left:38px;top:48px;font-size:24px;letter-spacing:.5px}
.board-brand .brand-dot{width:56px;height:56px}

.site{left:86px;top:169px;width:1028px;height:3391px;background:var(--white);box-shadow:0 0 18px rgba(5,146,205,.12)}
.nav{left:0;top:0;width:1028px;height:52px;background:var(--white)}
.nav .brand{position:absolute;left:148px;top:13px;font-size:11px;gap:7px}
.nav .brand-dot{width:26px;height:26px}
.nav-links{position:absolute;left:483px;top:19px;display:flex;gap:33px;font-size:10px;color:#333;list-style:none}
.nav-links .active{font-weight:700}

.hero{left:0;top:52px;width:1028px;height:527px;background:linear-gradient(135deg,#5f93ad 0%,#3f7d9f 45%,#2f6a8d 100%)}
.hero-photo{position:absolute;inset:0;background:linear-gradient(180deg,rgba(133,202,230,.35),rgba(5,146,205,.25))}
.hero h1{position:absolute;left:0;width:1028px;top:119px;text-align:center;color:#fff;font-size:35px;font-weight:600}
.hero p{position:absolute;left:0;width:1028px;top:172px;text-align:center;color:#fff;font-size:9px;font-weight:600;line-height:16px}
.btn{display:flex;align-items:center;justify-content:center;background:var(--blue);color:#fff;font-size:10px;font-weight:600;border-radius:2px}
.hero .btn{position:absolute;left:467px;top:217px;width:93px;height:31px;box-shadow:0 4px 10px rgba(0,0,0,.2)}

.features{left:86px;top:494px;width:856px;height:168px;background:#fff;box-shadow:0 6px 20px rgba(5,146,205,.12);display:flex;padding-top:40px}
.feature{flex:1;text-align:center;position:relative}
.feature+.feature::before{content:"";position:absolute;left:0;top:4px;height:70px;border-left:1px solid #ddd}
.feature svg{width:22px;height:22px}
.feature h3{font-size:10px;font-weight:600;margin-top:10px}
.feature p{font-size:8px;color:#555;line-height:12px;margin-top:12px}

.section-title{left:0;width:1028px;text-align:center;font-size:31px;font-weight:600}
.section-sub{left:0;width:1028px;text-align:center;font-size:9px;color:var(--muted);line-height:15px}

.approach h2{position:absolute;left:148px;top:871px;font-size:18px;font-weight:500}
.approach p{position:absolute;left:148px;top:905px;width:255px;font-size:9px;line-height:15px;color:var(--muted)}
.arrow{position:absolute;width:18px;height:18px}
.photo{position:absolute;background:linear-gradient(135deg,#c9c2b5,#8c8579 60%,#5a5550);box-shadow:0 4px 12px rgba(0,0,0,.15)}

.it-band{left:0;top:1173px;width:1028px;height:435px;background:var(--band)}
.service{position:absolute;top:1395px;width:160px;text-align:center}
.service svg{width:40px;height:40px}
.service h3{font-size:10px;font-weight:600;margin-top:12px}
.service p{font-size:8px;color:var(--muted);line-height:13px;margin-top:9px}

.cloud-card{position:absolute;width:213px;height:163px;background:#f7f7f7;padding:14px 12px}
.cloud-card .icon{width:50px;height:50px;border-radius:50%;background:#fff;display:flex;align-items:center;justify-content:center;box-shadow:0 2px 6px rgba(0,0,0,.08)}
.cloud-card .num{position:absolute;right:14px;top:14px;font-size:50px;font-weight:500;color:var(--blue-light);opacity:.6;line-height:1}
.cloud-card h3{font-size:12.5px;font-weight:600;margin-top:18px}
.cloud-card p{font-size:7.5px;line-height:13px;color:var(--muted);margin-top:13px}
.cloud-card.featured{background:var(--blue);color:#fff}
.cloud-card.featured p{color:#fff}
.cloud-card.featured .num{color:#fff;opacity:.25}

.blue{left:0;top:2268px;width:1028px;height:1123px;background:var(--blue);color:#fff}
.blue .section-title{color:#fff;top:82px}
.blue .kicker{position:absolute;left:0;width:1028px;top:131px;text-align:center;font-size:8px;font-weight:600}
.quote{position:absolute;left:0;width:1028px;top:264px;text-align:center;font-style:italic;font-size:19.5px;line-height:29px}
.author{position:absolute;left:0;width:1028px;top:376px;text-align:center;font-size:12px;font-weight:700}
.author span{font-size:9px;font-weight:400}

.contact{position:absolute;left:149px;top:545px;width:731px;height:360px;background:#fff;color:var(--ink)}
.contact h2{position:absolute;left:37px;top:68px;font-size:15px;font-weight:500;line-height:18px}
.field{position:absolute;left:37px;width:238px;background:var(--field);font-size:7px;color:#999;padding:10px 16px}
.contact .btn{position:absolute;left:37px;top:264px;width:77px;height:29px;font-size:8px;box-shadow:0 4px 10px rgba(5,146,205,.35)}
.office-photo{position:absolute;left:307px;top:0;width:424px;height:360px;background:linear-gradient(180deg,#c4d8ea 0%,#a86a4d 45%,#6a5a3a 75%,#4b5a3c 100%)}

.footer .brand{position:absolute;left:148px;top:950px;font-size:11px;color:#fff;gap:8px}
.footer .brand-dot{width:30px;height:30px;background:var(--blue-light)}
.footer-links{position:absolute;left:148px;top:1006px;display:flex;gap:15px;font-size:8.5px;list-style:none}
.news-label{position:absolute;left:635px;top:974px;font-size:9px;font-weight:600}
.news-input{position:absolute;left:635px;top:996px;width:145px;height:34px;background:#fff;color:#777;font-size:7.5px;padding:12px 20px}
.news-btn{position:absolute;left:785px;top:996px;width:95px;height:34px;background:#2b2b2b;color:#fff;font-size:9px;display:flex;align-items:center;justify-content:center}
.footer-rule{position:absolute;left:148px;top:1060px;width:732px;border-top:1px solid rgba(255,255,255,.35)}
.legal{position:absolute;left:148px;top:1078px;font-size:6px;display:flex;gap:10px}
.copyright{position:absolute;right:148px;top:1078px;font-size:6px}
</style>
</head>
<body>

<div class="abs brand board-brand"><span class="brand-dot"></span>Brindle KTR</div>

<main class="abs site">
  <header class="abs nav">
    <div class="brand"><span class="brand-dot"></span>Brindle KTR</div>
    <ul class="nav-links">
      <li class="active">Home</li><li>About Us</li><li>IT Support</li><li>Cloud Adoption</li><li>Contact Us</li>
    </ul>
  </header>

  <section class="abs hero">
    <div class="hero-photo" role="img" aria-label="Team of colleagues joining hands over a meeting table, blue tinted"></div>
    <h1>Experienced, Personalised IT Consulting</h1>
    <p>We understand that no two businesses are the same so why should the service delivered be any different.<br>We aim to understand all your business drivers so advise you every step of the way.</p>
    <div class="btn">Get Started</div>
  </section>

  <section class="abs features">
    <div class="feature">
      <svg viewBox="0 0 24 24" fill="none" stroke="#0592cd" stroke-width="1.2"><circle cx="12" cy="12" r="9"/><path d="M12 6v6l4 2"/></svg>
      <h3>Save Time</h3><p>We can allow you to<br>focus solely on growing</p>
    </div>
    <div class="feature">
      <svg viewBox="0 0 24 24" fill="none" stroke="#0592cd" stroke-width="1.2"><circle cx="11" cy="12" r="8"/><path d="M11 7v5h4"/><circle cx="18" cy="18" r="3"/></svg>
      <h3>24/7 Support</h3><p>Allow us to deliver the<br>support and expertise.</p>
    </div>
    <div class="feature">
      <svg viewBox="0 0 24 24" fill="none" stroke="#0592cd" stroke-width="1.2"><path d="M3 20h18M5 17l5-5 3 3 6-7"/><path d="M15 8h4v4"/></svg>
      <h3>Budgeting</h3><p>Take out the support<br>contract that best suits</p>
    </div>
    <div class="feature">
      <svg viewBox="0 0 24 24" fill="none" stroke="#0592cd" stroke-width="1.2"><circle cx="12" cy="5" r="2.5"/><circle cx="6" cy="17" r="2.5"/><circle cx="12" cy="17" r="2.5"/><circle cx="18" cy="17" r="2.5"/><path d="M12 8v6M6 14v-3h12v3"/></svg>
      <h3>Risk Management</h3><p>Leave us to protect your<br>business, if there is an</p>
    </div>
  </section>

  <h2 class="abs section-title" style="top:742px">About Us</h2>
  <p class="abs section-sub" style="top:788px">We understand that no two businesses are the same so why should the service delivered be any different.<br>We aim to understand all your business drivers so advise you every step of the way.</p>

  <div class="approach">
    <h2>Our Approach</h2>
    <p>We understand that no two businesses are the same so why should the service delivered be any different. We aim to understand all your business drivers so we can not only add a world class services but be there to advise you every step of the way.</p>
    <svg class="arrow" style="left:148px;top:1020px" viewBox="0 0 20 20" fill="none" stroke="#85cae6" stroke-width="1.3"><circle cx="10" cy="10" r="9"/><path d="M11.5 6l-4 4 4 4M7.5 10h6"/></svg>
    <svg class="arrow" style="left:183px;top:1020px" viewBox="0 0 20 20" fill="none" stroke="#0592cd" stroke-width="1.6"><circle cx="10" cy="10" r="9"/><path d="M8.5 6l4 4-4 4M6.5 10h6"/></svg>
  </div>
  <div class="photo" style="left:518px;top:871px;width:228px;height:167px" role="img" aria-label="Colleagues working with laptops around a meeting table"></div>
  <div class="photo" style="left:769px;top:943px;width:111px;height:78px" role="img" aria-label="Small team discussion in an office"></div>
  <div class="photo" style="left:687px;top:1024px;width:146px;height:69px" role="img" aria-label="Business meeting in a conference room"></div>

  <section class="abs it-band"></section>
  <h2 class="abs section-title" style="top:1253px">IT Support</h2>
  <p class="abs section-sub" style="top:1300px">We understand that no two businesses are the same so why should the service delivered be any different.<br>We aim to understand all your business drivers so advise you every step of the way.</p>

  <div class="service" style="left:145px">
    <svg viewBox="0 0 40 40" fill="none" stroke="#0592cd" stroke-width="1.2"><path d="M3 20c5-8 11-11 17-11s12 3 17 11c-5 8-11 11-17 11S8 28 3 20z"/><circle cx="20" cy="20" r="7"/><circle cx="20" cy="20" r="3"/></svg>
    <h3>Proactive Monitoring</h3><p>We can allow you to focus solely on growing and developing your business.</p>
  </div>
  <div class="service" style="left:337px">
    <svg viewBox="0 0 40 40" fill="none" stroke="#0592cd" stroke-width="1.2"><path d="M20 4l13 5v10c0 9-6 14-13 17C13 33 7 28 7 19V9z"/><rect x="15" y="19" width="10" height="8"/><path d="M17 19v-3a3 3 0 016 0v3"/></svg>
    <h3>Security and Data Back-up</h3><p>We can allow you to focus solely on growing and developing your business.</p>
  </div>
  <div class="service" style="left:530px">
    <svg viewBox="0 0 40 40" fill="none" stroke="#0592cd" stroke-width="1.2"><circle cx="20" cy="14" r="8"/><path d="M16 14l3 3 5-5M8 36c0-7 5-11 12-11s12 4 12 11"/></svg>
    <h3>Built-in Compliance (GDPR)</h3><p>We can allow you to focus solely on growing and developing your business.</p>
  </div>
  <div class="service" style="left:722px">
    <svg viewBox="0 0 40 40" fill="none" stroke="#0592cd" stroke-width="1.2"><circle cx="20" cy="20" r="16"/><circle cx="20" cy="20" r="10"/><circle cx="20" cy="17" r="3"/><path d="M15 25c1-3 3-4 5-4s4 1 5 4M20 4v6M20 30v6M4 20h6M30 20h6"/></svg>
    <h3>Responsive IT Support</h3><p>We can allow you to focus solely on growing and developing your business.</p>
  </div>

  <h2 class="abs section-title" style="top:1687px">Cloud Adoption</h2>
  <p class="abs section-sub" style="top:1733px">We understand that no two businesses are the same so why should the service delivered be any different.<br>We aim to understand all your business drivers so advise you every step of the way.</p>

  <div class="cloud-card featured" style="left:149px;top:1815px">
    <div class="icon"><svg width="28" height="28" viewBox="0 0 28 28" fill="none" stroke="#0592cd" stroke-width="1.2"><circle cx="9" cy="9" r="4"/><circle cx="19" cy="19" r="4"/><path d="M17 5a6 6 0 015 5M11 23a6 6 0 01-5-5"/></svg></div>
    <span class="num">1</span>
    <h3>Services. Perfectly Managed</h3>
    <p>We employ Managed Services to significantly streamline your business, tailoring your solutions to meet digital market demands.</p>
  </div>
  <div class="cloud-card" style="left:407px;top:1815px">
    <div class="icon"><svg width="28" height="28" viewBox="0 0 28 28" fill="none" stroke="#0592cd" stroke-width="1.2"><circle cx="14" cy="14" r="10"/><path d="M9 14a5 5 0 019-3M19 14a5 5 0 01-9 3"/></svg></div>
    <span class="num">2</span>
    <h3>Fail Fast with the Cloud</h3>
    <p>Prototype your new business features within less than a week &amp; without having to invest a single penny.</p>
  </div>
  <div class="cloud-card" style="left:666px;top:1815px">
    <div class="icon"><svg width="28" height="28" viewBox="0 0 28 28" fill="none" stroke="#0592cd" stroke-width="1.2"><path d="M8 20a5 5 0 010-10 7 7 0 0113 1 4.5 4.5 0 010 9z"/><path d="M12 20v-4M15 20v-6M18 20v-3"/></svg></div>
    <span class="num">3</span>
    <h3>Improve your ROI</h3>
    <p>Using the Cloud, we launch your product to market quickly and cost-effectively – making sure it's future-proof, scalable, reliable, and</p>
  </div>
  <div class="cloud-card" style="left:279px;top:2025px">
    <div class="icon"><svg width="28" height="28" viewBox="0 0 28 28" fill="none" stroke="#0592cd" stroke-width="1.2"><path d="M8 19a5 5 0 010-10 7 7 0 0113 1 4.5 4.5 0 010 9z"/><path d="M14 23v-9M11 17l3-3 3 3"/></svg></div>
    <span class="num">4</span>
    <h3>The Cloud Dream Team</h3>
    <p>They'll have thorough understanding of the project's scope. They'll see the bigger picture and understand the business value you want</p>
  </div>
  <div class="cloud-card" style="left:538px;top:2025px">
    <div class="icon"><svg width="28" height="28" viewBox="0 0 28 28" fill="none" stroke="#0592cd" stroke-width="1.2"><ellipse cx="18" cy="10" rx="5" ry="2"/><path d="M13 10v10c0 1 2 2 5 2s5-1 5-2V10M13 15c0 1 2 2 5 2s5-1 5-2"/><path d="M5 22v-5M9 22v-8M4 12l4-4 3 2"/></svg></div>
    <span class="num">5</span>
    <h3>The Business Benefits</h3>
    <p>Make informed decisions about the product's development pipeline. Save costs as you'll spend less time on redefining requirements.</p>
  </div>

  <section class="abs blue">
    <h2 class="abs section-title">Testimonials</h2>
    <p class="kicker">What our clint say about us</p>
    <svg class="abs" style="left:491px;top:200px" width="46" height="40" viewBox="0 0 46 40" fill="none" stroke="#fff" stroke-width="2"><path d="M4 38V18a12 12 0 0124 0 8 8 0 01-14 0"/><path d="M20 38V18a12 12 0 0124 0 8 8 0 01-14 0"/></svg>
    <p class="quote">Our extensive equipment fleet, along with our modern maintenance and<br>fabrication facility allow us the ability to support our diverse workforce and<br>our capable partners whenever necessary.</p>
    <p class="author">Owen Hardcastle <span>- Pellow Client</span></p>
    <svg class="arrow" style="left:149px;top:375px" viewBox="0 0 20 20" fill="none" stroke="#fff" stroke-width="1.3"><circle cx="10" cy="10" r="9"/><path d="M11.5 6l-4 4 4 4M7.5 10h6"/></svg>
    <svg class="arrow" style="left:861px;top:375px" viewBox="0 0 20 20" fill="none" stroke="#fff" stroke-width="1.3"><circle cx="10" cy="10" r="9"/><path d="M8.5 6l4 4-4 4M6.5 10h6"/></svg>

    <div class="contact">
      <h2>Let's Make a Call<br>Request</h2>
      <div class="field" style="top:128px;height:27px">Your Name</div>
      <div class="field" style="top:162px;height:27px">Phone Number</div>
      <div class="field" style="top:195px;height:53px;padding-top:24px">Write Message</div>
      <div class="btn">Get Started</div>
      <div class="office-photo" role="img" aria-label="Thornwick Lodge, a red-brick manor house beside water"></div>
    </div>

    <footer class="footer">
      <div class="brand"><span class="brand-dot"></span>Brindle KTR</div>
      <ul class="footer-links"><li>Home</li><li>About Us</li><li>IT Support</li><li>Cloud Adoption</li><li>Contact Us</li></ul>
      <p class="news-label">Get the freshest news from us</p>
      <div class="news-input">Your email address...</div>
      <div class="news-btn">Subscribe</div>
      <div class="footer-rule"></div>
      <p class="legal"><span>Terms &amp; Conditions</span>|<span>Privacy Policy</span>|<span>Accessibility</span>|<span>Legal</span></p>
      <p class="copyright">Brindle KTR 2020, All right reserved</p>
    </footer>
  </section>
</main>
</body>
</html>
```